TalvoMesh

Hey

I am involved with crowd funding, please look at one of my current sites www.pennorift.com
Work is currently under way with a new site www.talvomesh.com .wehave the basics but I am not happy with what we have so far. I need to redesign the web site but keep the concept . The cartoon pitch will be kept , along with some of the other functions which we can help you with, unless you are able to build / design something better. I liked a lot of the designs submitted for a previous crowd funning design, far better than what I currently have. To be included on this site will be links to numerous crowd funding sites which I have registered but each site will be focused on a specific topic which will be disclosed once this site is active. I intend to build all these sites through this site. Along with these sites will be a logo design for each site so plenty of work going forward. I have a logo for talvomesh already but am open for improvements and suggestions but would like to keep a map or logo of Africa included in the design. To bear in mind this is a African focused buisness which aims to help communities, employment creation, poverty alleviation and help young entrepreneurs kickstarter their buisness . I already have a group logo , which was designed on this site ( look at brelo yards competition) , I would like this logo to be used on all the site so customers and investors link the group and concept togeather. Here is the link http://www.quillmarta.co.uk/project-progress.aspx?briefId=48213 . I have removed the breloyard from the bottom of the logo and will just be using the figurines as the group logo on all web sites. There will be at least fifty related crowd fund projects linked to this site.
If any body has any questions or ideas please feel free to ask for anything you may need. Thanks to everybody who helps with this project. Warmly. Owen
Updates

Hi everyone working on my design.

The contact details to use on the site are

27 Velder Grove
Marnsdal
Cape Town 
+263745208839
+447911463052

E mail enquiries@TalvoMesh.example

There are two logos, one is the talvomesh logo and the other is my group logo which I will attach to the pitch
Good luck and thank you to everybody who is working on this web design
Warmly

Owen

Industry/Entity Type

Build

```html
<!DOCTYPE html>
<html lang="en">
<head>
<meta charset="utf-8">
<title>TalvoMesh – Crowdfunding</title>
<link href="https://fonts.googleapis.com/css2?family=Lato:wght@300;400;700;900&display=swap" rel="stylesheet">
<style>
:root{
  --blue:#0a8fd8;
  --blue-dark:#0577b8;
  --link:#0f7fc4;
  --ink:#2b2b2b;
  --muted:#4a4a4a;
  --bar:#1f1f1f;
  --footer:#262626;
  --header-grey:#eeeeee;
  --page:#f3f3f3;
  --white:#ffffff;
}
*{margin:0;padding:0;box-sizing:border-box}
html,body{width:1086px;height:1200px;overflow:hidden}
body{
  position:relative;font-family:"Lato",sans-serif;color:var(--ink);
  background:radial-gradient(ellipse at 50% 40%,#ffffff 0%,#f1f1f1 55%,#e4e4e4 100%);
}
.abs{position:absolute}
/* top nav */
.topnav{left:0;top:0;width:1086px;height:29px;background:var(--white);border-bottom:1px solid #d6d6d6}
.topnav ul{list-style:none;position:absolute;left:426px;top:9px;display:flex;gap:27px;font-size:9px;color:#333;letter-spacing:-.1px}
/* header band */
.header{left:0;top:29px;width:1086px;height:96px;background:var(--header-grey);border-bottom:1px solid #dcdcdc}
.brand{left:177px;top:42px;display:flex;flex-direction:column;align-items:center;gap:8px}
.brand-mark{width:36px;height:36px;border-radius:50%;background:var(--blue)}
.brand-name{font-size:19px;font-weight:400;color:var(--blue-dark)}
.intro{left:458px;top:52px;width:365px;font-size:9px;line-height:16.5px;color:#444}
/* hero */
.hero{left:178px;top:125px;width:730px;height:191px;display:flex}
.hero-left{width:290px;height:100%;background:linear-gradient(135deg,#6d6b3a,#a1533e 55%,#3f3a2a)}
.hero-right{flex:1;height:100%;background:radial-gradient(ellipse at 55% 55%,#f7b63a 0%,#e07a12 45%,#8a3a06 100%)}
.arrow{top:213px;width:12px;height:14px}
/* login bar */
.loginbar{left:178px;top:335px;width:730px;height:36px;background:var(--bar);color:#fff;font-size:10.5px}
.loginbar .item{top:13px;font-weight:300}
.divider{top:0;width:1px;height:36px;background:#4a4a4a}
.field{top:10px;width:95px;height:18px;background:#fff;color:#222;font-size:10px;padding:3px 5px;border:1px solid #999}
.btn-login{left:537px;top:10px;width:65px;height:18px;background:var(--blue);font-weight:700;font-size:10.5px;text-align:center;line-height:18px}
.btn-social{left:618px;top:6px;width:107px;height:15px;background:#3a6db5;font-size:8px;line-height:15px;padding-left:19px}
.btn-social::before{content:"";position:absolute;left:4px;top:3px;width:9px;height:9px;background:#fff}
.register{left:618px;top:27px;font-size:7px;font-weight:700}
/* cards */
.card{top:392px;width:167px}
.card-img{width:167px;height:155px;background:linear-gradient(180deg,#4f86c9 0%,#a9c9ea 28%,#8f9aa3 52%,#5a6066 100%);position:relative}
.card-stat{position:absolute;left:0;bottom:0;width:167px;height:37px;background:rgba(235,235,235,.88);font-size:10.5px;line-height:13px;padding:5px 5px;color:#222}
.card-stat .ratio{position:absolute;right:30px;top:11px;font-size:15px;font-weight:900}
.card-stat svg{position:absolute;right:8px;top:9px}
.card-title{margin-top:13px;font-size:11.5px;font-weight:700;color:var(--link);text-decoration:underline}
.card-text{margin-top:7px;font-size:8.7px;line-height:12.5px;color:#333}
/* welcome */
.welcome{left:177px;top:677px;width:541px;height:206px;background:var(--blue);color:#fff;box-shadow:0 10px 14px -6px rgba(0,0,0,.35)}
.welcome h1{position:absolute;left:15px;top:16px;font-size:18.5px;font-weight:300;line-height:22px}
.welcome h1 b{font-weight:700}
.welcome p{position:absolute;left:15px;top:71px;width:222px;font-size:9.6px;line-height:14.8px}
.video{left:265px;top:21px;width:253px;height:164px;background:linear-gradient(160deg,#9c9c9c,#6d6d6d);}
.video-controls{position:absolute;left:0;bottom:0;width:100%;height:16px;background:#1d1d1d;font-size:7px;font-weight:700;color:#fff}
.share{position:absolute;right:8px;top:8px;width:48px;height:48px;background:#2a2a2a;border:1px solid #777;border-radius:4px;font-size:8px;text-align:center;padding-top:32px}
.play{position:absolute;left:103px;top:48px;width:48px;height:42px;background:rgba(30,30,30,.75);border-radius:5px}
/* side panels */
.panel{left:741px;width:167px;background:#fff;box-shadow:0 2px 4px rgba(0,0,0,.15)}
.panel h2{height:29px;background:var(--blue);color:#fff;font-size:19px;font-weight:700;padding:4px 7px;line-height:22px}
.panel p{font-size:8.7px;line-height:12.8px;color:#333;padding:4px 7px 6px}
/* categories */
.cat-title{left:177px;top:906px;font-size:19px;font-weight:700;color:var(--link)}
.cat{font-size:12.5px;color:var(--link);line-height:15px}
/* bands */
.contactband{left:0;top:1051px;width:1086px;height:18px;background:var(--blue);color:#fff;font-size:12px;text-align:center;line-height:18px;font-weight:300}
.contactband a{color:#fff;font-weight:700;text-decoration:underline}
.footer{left:0;top:1079px;width:1086px;height:121px;background:linear-gradient(180deg,#2e2e2e,#1a1a1a);color:#fff;font-size:8.5px;line-height:13px}
.footer .col{top:12px}
.footer .email{left:171px;top:95px;font-weight:700}
.footer .rule{left:265px;top:14px;width:1px;height:66px;background:#888}
.soc{top:19px;width:23px;height:23px;border-radius:3px}
.badge{top:58px;height:40px}
</style>
</head>
<body>

<nav class="topnav abs">
  <ul>
    <li>BLOG</li><li>IPO'S</li><li>HOW IT WORKS</li><li>ABOUT</li><li>MY ACCOUNT</li><li>MY CART</li><li>more@talvomesh.com</li>
  </ul>
</nav>

<header class="header abs"></header>
<div class="brand abs">
  <span class="brand-mark"></span>
  <span class="brand-name">BreloYards</span>
</div>
<p class="intro abs">Ground rules are simple; JOIN, send us a Vidrella or any other video link to any idea. It can be an idea just floating around or an idea which has already come to life. No catches, no entry fee, no award collection fee, only one entry per member.</p>

<section class="hero abs">
  <div class="hero-left" role="img" aria-label="Photo of a woman and local children looking at crafts together"></div>
  <div class="hero-right" role="img" aria-label="Photo of elephants walking under acacia trees at an orange sunset"></div>
</section>
<svg class="arrow abs" style="left:160px" viewBox="0 0 12 14"><path d="M9 1 L3 7 L9 13" fill="none" stroke="#999" stroke-width="2.5"/></svg>
<svg class="arrow abs" style="left:914px" viewBox="0 0 12 14"><path d="M3 1 L9 7 L3 13" fill="none" stroke="#999" stroke-width="2.5"/></svg>

<section class="loginbar abs">
  <span class="item abs" style="left:22px">Join Now</span>
  <span class="item abs" style="left:107px">How it works?</span>
  <span class="item abs" style="left:214px">Browse Companies</span>
  <span class="divider abs" style="left:330px"></span>
  <span class="field abs" style="left:342px">Username</span>
  <span class="field abs" style="left:440px;letter-spacing:1px">•••••••••</span>
  <span class="btn-login abs">LOGIN</span>
  <span class="divider abs" style="left:612px"></span>
  <span class="btn-social abs">Sign in with Linkora</span>
  <span class="register abs">Register I Forgotten Password</span>
</section>

<!-- project cards -->
<article class="card abs" style="left:178px">
  <div class="card-img" role="img" aria-label="Photo of a city skyline under a blue sky">
    <div class="card-stat">Funded $<br>Goal $ 1,000<span class="ratio">0X</span>
      <svg width="18" height="18" viewBox="0 0 18 18"><circle cx="4.5" cy="3" r="2.2"/><rect x="2" y="6" width="5" height="11" rx="1"/><circle cx="13.5" cy="3" r="2.2"/><rect x="11" y="6" width="5" height="11" rx="1"/></svg></div>
  </div>
  <h3 class="card-title">Ut placcerat numc suscipit</h3>
  <p class="card-text">Ut placerat nunc suscipit metus lacinia vel interdum tortor eleifend. Aliquam erat volutpat. Ut consectetur auctor ornare. Donec molestie eros id lacus porta tempus. Phasellus... »</p>
</article>
<article class="card abs" style="left:366px">
  <div class="card-img" role="img" aria-label="Photo of a city skyline under a blue sky">
    <div class="card-stat">Funded $<br>Goal $ 500<span class="ratio">0X</span>
      <svg width="18" height="18" viewBox="0 0 18 18"><circle cx="4.5" cy="3" r="2.2"/><rect x="2" y="6" width="5" height="11" rx="1"/><circle cx="13.5" cy="3" r="2.2"/><rect x="11" y="6" width="5" height="11" rx="1"/></svg></div>
  </div>
  <h3 class="card-title">Proin in ante et nulla</h3>
  <p class="card-text">Proin in ante et nulla mollis faucibus non sit amet felis. Vestibulum ac eros risus. Nullam turpis orci, ornare vitae porta vitae, fringilla vitae sem.... »</p>
</article>
<article class="card abs" style="left:553px">
  <div class="card-img" role="img" aria-label="Photo of a city skyline under a blue sky">
    <div class="card-stat">Funded $<br>Goal $ 4,000<span class="ratio">0X</span>
      <svg width="18" height="18" viewBox="0 0 18 18"><circle cx="4.5" cy="3" r="2.2"/><rect x="2" y="6" width="5" height="11" rx="1"/><circle cx="13.5" cy="3" r="2.2"/><rect x="11" y="6" width="5" height="11" rx="1"/></svg></div>
  </div>
  <h3 class="card-title">Vestibulum sed nulla</h3>
  <p class="card-text">Vestibulum sed nulla in ipsum venenatis semper. Pellentesque ut leo sed lorem lobortis semper ac ut risus. Cum sociis natoque penatibus et magnis dis parturient... »</p>
</article>
<article class="card abs" style="left:741px">
  <div class="card-img" role="img" aria-label="Photo of a city skyline under a blue sky">
    <div class="card-stat">Funded $ 2<br>Goal $ 1<span class="ratio">2X</span>
      <svg width="18" height="18" viewBox="0 0 18 18"><circle cx="4.5" cy="3" r="2.2"/><rect x="2" y="6" width="5" height="11" rx="1"/><circle cx="13.5" cy="3" r="2.2"/><rect x="11" y="6" width="5" height="11" rx="1"/></svg></div>
  </div>
  <h3 class="card-title">The elephant with on trunk</h3>
  <p class="card-text">The elephant with no trunk. They say that a picture paints a thousand words, but no words can describe the pain, the anguish and the... »</p>
</article>

<section class="welcome abs">
  <h1>Welcome to <b>Africa’s</b><br>leading crowdfunding site.</h1>
  <p>What is Crowdfunding?<br>Crowdfunding enables people to raise money for innovative new projects by getting like-minded individuals to pool their money to back the idea, person or business. It’s a way to make things happen.</p>
  <div class="video abs" role="img" aria-label="Animated cartoon pitch video">
    <div class="play"><svg width="48" height="42" viewBox="0 0 48 42"><path d="M19 12 L33 21 L19 30 Z" fill="#fff"/></svg></div>
    <div class="share">
      <svg class="abs" style="left:15px;top:8px" width="18" height="18" viewBox="0 0 18 18"><circle cx="14" cy="3.5" r="2.8" fill="#fff"/><circle cx="4" cy="9" r="2.8" fill="#fff"/><circle cx="14" cy="14.5" r="2.8" fill="#fff"/><path d="M14 3.5 L4 9 L14 14.5" stroke="#fff" stroke-width="1.5" fill="none"/></svg>share</div>
    <div class="video-controls">
      <svg class="abs" style="left:9px;top:4px" width="8" height="8" viewBox="0 0 8 8"><path d="M1 0 L8 4 L1 8Z" fill="#fff"/></svg>
      <span class="abs" style="left:26px;top:4px">00:00</span>
      <span class="abs" style="left:58px;top:7px;width:124px;height:2px;background:#666"></span>
      <span class="abs" style="left:189px;top:4px">00:00</span>
      <svg class="abs" style="left:218px;top:4px" width="9" height="8" viewBox="0 0 9 8"><path d="M0 2.5H2.5L5 0V8L2.5 5.5H0Z M6.5 2 Q8 4 6.5 6" fill="#fff" stroke="#fff" stroke-width=".8"/></svg>
      <svg class="abs" style="left:236px;top:4px" width="8" height="8" viewBox="0 0 8 8"><path d="M1 1 L7 7 M1 1 H4 M1 1 V4 M7 7 H4 M7 7 V4" stroke="#fff" stroke-width="1.2" fill="none"/></svg>
    </div>
  </div>
</section>

<aside class="panel abs" style="top:677px">
  <h2>FUND</h2>
  <p>The elephant with no trunk. They say that a picture paints a thousand words, but no words can describe the pain, the anguish and the... »</p>
</aside>
<aside class="panel abs" style="top:784px">
  <h2>JOIN</h2>
  <p>The elephant with no trunk. They say that a picture paints a thousand words, but no words can describe the pain, the anguish and the... »</p>
</aside>

<h2 class="cat-title abs">BUSINESS CATEGORIES</h2>
<span class="cat abs" style="left:177px;top:949px">COMICS</span>
<span class="cat abs" style="left:177px;top:978px">ENVIRONMENT</span>
<span class="cat abs" style="left:177px;top:1008px">FASHION</span>
<span class="cat abs" style="left:327px;top:949px">FILM AND VIDEO</span>
<span class="cat abs" style="left:327px;top:978px">GAMING</span>
<span class="cat abs" style="left:327px;top:1008px">HEALTH AND FITNESS</span>
<span class="cat abs" style="left:513px;top:949px">INTERNET, IT AND<br>TELECOMULICATIONS</span>
<span class="cat abs" style="left:513px;top:993px">LEISURE AND TOURISM</span>
<span class="cat abs" style="left:513px;top:1023px">MUSIC</span>
<span class="cat abs" style="left:707px;top:949px">PROFESSIONAL SERVICES</span>
<span class="cat abs" style="left:707px;top:978px">TECHNOLOGY</span>

<div class="contactband abs">Would you like to know <a>more@nestarloop.example</a> ?</div>

<footer class="footer abs">
  <address class="col abs" style="left:171px;font-style:normal">27 Velder Grove<br>Marnsdal<br>Cape Town<br>+263745208839<br>+447911463052</address>
  <span class="rule abs"></span>
  <ul class="col abs" style="left:290px;list-style:none">
    <li>Terms and Conditions</li><li>Privacy Policy</li><li>Join Now</li><li>How it works?</li><li>Browse Companies</li>
  </ul>
  <span class="email abs">E mail enquiries@TalvoMesh.example</span>
  <span class="soc abs" style="left:757px;background:#3b5b9b"></span>
  <span class="soc abs" style="left:789px;background:#3fa6d8"></span>
  <span class="soc abs" style="left:821px;background:#1a76b3"></span>
  <span class="soc abs" style="left:853px;background:#c9302a"></span>
  <span class="soc abs" style="left:885px;background:#e6e6e6"></span>
  <span class="badge abs" style="left:563px;width:145px;border-radius:20px 4px 4px 20px;background:#17a05a"></span>
  <span class="badge abs" style="left:722px;width:75px;top:63px;height:28px;border-radius:14px;background:#f2f2f2"></span>
  <span class="badge abs" style="left:813px;width:95px;top:63px;height:30px;background:#f7f7f7"></span>
</footer>

</body>
</html>
```